Torvel, Inc. new buisness cards - brand guide included

We need new business cards. SLEAK SIMPLE FINANCE. They must include a place for NAME, TITLE, CELL, OFFICE PHONE, EMAIL. they also must include our services across the bottom. AIR, OCEAN, FTL, LTL, EXPRESS. for reference this will be being handed to some of the most prestigious shipping companies in a america.

Target Market(s)

Finance and corporate

Contact Information for Business Card

We need new business cards. SLEAK SIMPLE FINANCE. They must include a place for NAME, TITLE, CELL, OFFICE PHONE, EMAIL. they also must include our services across the bottom. AIR, OCEAN, FTL, LTL, EXPRESS.

Requirements
Must have
• We need new business cards. SLEAK SIMPLE FINANCE. They must include a place for NAME, TITLE, CELL, OFFICE PHONE, EMAIL. they also must include our services across the bottom. AIR, OCEAN, FTL, LTL, EXPRESS.
Nice to have
• USE THE COLORS AND LOGO IN THE BRAND GUIDE :)

```html
<!DOCTYPE html>
<html lang="en">
<head>
<meta charset="utf-8">
<title>Torvel, Inc. — Business Card</title>
<link rel="stylesheet" href="https://fonts.googleapis.com/css2?family=Poppins:wght@400;500;600&display=swap">
<style>
  :root {
    --backdrop: #e8e4dd;
    --card: #353535;
    --tan: #c3b59b;
    --white: #ffffff;
    --silver: #a9a9a9;
  }
  * { margin: 0; padding: 0; box-sizing: border-box; }
  html, body { width: 916px; height: 1200px; overflow: hidden; }
  body {
    background: var(--backdrop);
    font-family: "Poppins", sans-serif;
    position: relative;
  }
  .card {
    position: absolute;
    left: 71px;
    width: 777px;
    height: 463px;
    background: var(--card);
    border-radius: 22px;
    overflow: hidden;
  }
  .card-front { top: 107px; }
  .card-back { top: 640px; }

  .front-wordmark {
    position: absolute;
    left: 0; right: 0;
    top: 175px;
    text-align: center;
    font-size: 96px;
    font-weight: 500;
    letter-spacing: 10px;
    line-height: 1;
    color: var(--silver);
  }
  .back-wordmark {
    position: absolute;
    right: 45px;
    top: 70px;
    font-size: 58px;
    font-weight: 500;
    letter-spacing: 5px;
    line-height: 1;
    color: var(--tan);
  }
  .holder { position: absolute; left: 42px; top: 232px; }
  .holder-name {
    font-size: 26px;
    font-weight: 600;
    color: var(--tan);
    line-height: 1.1;
  }
  .holder-title {
    font-size: 16px;
    color: var(--white);
    line-height: 1.2;
  }
  .divider {
    position: absolute;
    left: 42px; right: 24px;
    top: 283px;
    height: 2px;
    background: var(--tan);
  }
  .contacts {
    position: absolute;
    left: 42px; top: 297px;
    list-style: none;
  }
  .contacts li {
    display: flex;
    align-items: center;
    height: 25.5px;
    font-size: 16px;
    color: var(--white);
  }
  .contacts .icon {
    width: 20px; height: 20px;
    margin-right: 9px;
    flex: none;
  }
  .address {
    position: absolute;
    left: 510px; top: 343px;
    font-size: 15.5px;
    line-height: 22px;
    color: var(--white);
  }
  .services {
    position: absolute;
    left: 0; right: 0;
    top: 410px;
    height: 37px;
    background: var(--tan);
    display: flex;
    justify-content: center;
    align-items: center;
    gap: 14px;
    list-style: none;
    font-size: 15px;
    color: var(--white);
    letter-spacing: 0.5px;
  }
  .services li::before {
    content: "";
    display: inline-block;
    width: 6px; height: 6px;
    border-radius: 50%;
    background: var(--white);
    margin-right: 8px;
    vertical-align: middle;
    position: relative; top: -2px;
  }
</style>
</head>
<body>

<section class="card card-front">
  <div class="front-wordmark">TORVEL</div>
</section>

<section class="card card-back">
  <div class="back-wordmark">TORVEL</div>

  <div class="holder">
    <p class="holder-name">Daniel Hart</p>
    <p class="holder-title">Head contractor</p>
  </div>

  <div class="divider"></div>

  <ul class="contacts">
    <li>
      <svg class="icon" viewBox="0 0 20 20"><circle cx="10" cy="10" r="10" fill="#c3b59b"/><path d="M6 8.5c0-1.5 1.8-2.5 4-2.5s4 1 4 2.5l-1.6.4-.4-1.2c-1.3-.5-2.7-.5-4 0l-.4 1.2zM7 10h6l1 4H6z" fill="#353535"/></svg>
      555-201-4870
    </li>
    <li>
      <svg class="icon" viewBox="0 0 20 20"><circle cx="10" cy="10" r="10" fill="#c3b59b"/><rect x="7" y="4.5" width="6" height="11" rx="1" fill="#353535"/><rect x="8" y="6" width="4" height="7" fill="#c3b59b"/></svg>
      555-201-4870
    </li>
    <li>
      <svg class="icon" viewBox="0 0 20 20"><circle cx="10" cy="10" r="10" fill="#c3b59b"/><rect x="5" y="6.5" width="10" height="7" rx="1" fill="#ffffff"/><path d="M5.5 7l4.5 3.5L14.5 7" stroke="#c3b59b" fill="none"/></svg>
      accounting@torvelinc.com
    </li>
    <li>
      <svg class="icon" viewBox="0 0 20 20"><circle cx="10" cy="10" r="10" fill="#c3b59b"/><circle cx="10" cy="10" r="5" fill="none" stroke="#353535" stroke-width="1.2"/><path d="M5 10h10M10 5c-2.5 3-2.5 7 0 10M10 5c2.5 3 2.5 7 0 10" stroke="#353535" stroke-width="1" fill="none"/></svg>
      www.torvelinc.com
    </li>
  </ul>

  <address class="address" style="font-style:normal">
    2840 Harbor View Rd Ste 110<br>
    Larkfield, WA 98120
  </address>

  <ul class="services">
    <li>AIR</li>
    <li>OCEAN</li>
    <li>FTL</li>
    <li>LTL</li>
    <li>EXPRESS</li>
  </ul>
</section>

</body>
</html>
```